New Consulting Firm News PowerPoint Template

We are a new consulting firm that specializes in Veltrix Unified Results Planning implementations in need of a new PowerPoint template. We need at least the following layouts:
• Main Cover Slide
• Agenda / Table of Contents
• Title slide for each of the agenda items leading into actual content
• Title + Content with nice bullets in the content
• Title + Sub-Title + Content with nice bullets in the content
• Title + Two Columns of Content
• Title + Sub-Title + Two Columns of Content
• Title + Three Columns of Content
• Title + Sub-Title + Three Columns of Content
• Title + Two Rows and Two Columns of Content (4 boxes)
• Title + Sub-Title + Two Rows and Two Columns of Content (4 boxes)
• Title + Blank
• Nascar Slide (Client logos arranged somehow)
• Case Study Slide
• Various infographic slides than can be used and modified would be amazing as well
Our logo has been uploaded and you can find our website here:
https://brankelladvisory.example
We would like the main theme colors to blend with our logo, but also have a variety of colors in the theme that compliment the main theme colors. Once we have selected a PowerPoint design we expect to immediately have a Word design contest and the winning PowerPoint design will likely be a heavy influence on the Word design.

Target Market(s)

CFO, CAO, VP of Finance, Controllers

Industry/Entity Type

Consulting

Font styles to use
Serif
Sans Serif

Requirements
Must have
• • Main Cover Slide
• Title + Blank
• Case Study Slide
Nice to have
• • Various infographic slides than can be used and modified would be amazing as well

```html
<!DOCTYPE html>
<html lang="en">
<head>
<meta charset="utf-8">
<title>Brankell Advisory – Presentation Template</title>
<link href="https://fonts.googleapis.com/css2?family=Cinzel:wght@600;700&family=Roboto:wght@400;700&display=swap" rel="stylesheet">
<style>
:root{
  --page:#e4e4e4;
  --blue:#2f7bc4;
  --blue-deep:#1e5fa3;
  --navy:#1a2f52;
  --gray:#6d6e71;
  --gray-dark:#58595b;
  --ink:#222;
  --muted:#8a8a8a;
  --white:#fff;
  --line:#e3e3e3;
}
*{box-sizing:border-box;margin:0;padding:0}
html,body{width:751px;height:1200px;overflow:hidden;background:var(--page)}
body{position:relative;font-family:"Roboto",Arial,sans-serif;color:var(--ink)}
.slide{position:absolute;width:329px;height:185px;background:var(--white);overflow:hidden;box-shadow:0 1px 2px rgba(0,0,0,.08)}
.col-l{left:31px}.col-r{left:391px}
.row-1{top:72px}.row-2{top:290px}.row-3{top:507px}.row-4{top:725px}.row-5{top:943px}
.abs{position:absolute}
.serif{font-family:"Cinzel",Georgia,serif;font-weight:700;letter-spacing:.3px}

/* header band */
.header{position:absolute;left:0;top:0;width:329px;height:23px}
.header-title{position:absolute;left:27px;top:5px;font-size:9px;color:var(--white)}
.brand-mini{position:absolute;left:276px;top:5px;width:46px;text-align:center;font-size:4px;font-weight:700;color:var(--blue);letter-spacing:.3px;line-height:1.2}
.brand-mini .mark{display:block;width:8px;height:8px;margin:0 auto 1px;background:var(--blue)}

/* footer */
.footer-line{position:absolute;left:27px;right:27px;top:171px;height:.5px;background:var(--line)}
.footer{position:absolute;left:27px;right:27px;top:176px;font-size:2.8px;color:#555;display:flex;justify-content:space-between}
.footer .page{color:var(--blue)}
.footer.on-blue,.footer.on-blue .page{color:var(--white)}
.base-line{position:absolute;left:0;right:0;bottom:0;height:1px;background:var(--blue)}

.h-item{font-size:4px;font-weight:700;color:var(--ink)}
.p{font-size:2.8px;line-height:1.55;color:var(--muted)}
.photo{position:absolute}

/* cover */
.cover-title{position:absolute;left:27px;top:34px;font-size:11px;line-height:15.5px;color:var(--white)}
.cover-brand{position:absolute;left:27px;top:148px;font-size:9px;font-weight:700;color:var(--blue);letter-spacing:1px}
.cover-brand .sub{display:block;font-size:3.4px;font-weight:400;color:var(--gray);letter-spacing:1.5px;text-align:center}
.socials{position:absolute;left:284px;top:169px;display:flex;gap:1.5px}
.socials span{width:6px;height:6px;border:.6px solid var(--ink);border-radius:50%}

/* list items slide 4 */
.icon-dot{position:absolute;width:16px;height:16px;border-radius:50%;border:1.5px solid #ddd}
.icon-dot.gray{background:var(--gray)}
.icon-dot.blue{background:var(--blue)}
.icon-dot::after{content:"";position:absolute;left:4px;top:4px;width:5px;height:5px;border:.8px solid var(--white);border-radius:50%}

.bullets{position:absolute;left:186px;top:72px;list-style:none}
.bullets li{font-size:2.8px;color:#555;height:7.05px;padding-left:7px;position:relative}
.bullets li::before{content:"";position:absolute;left:0;top:.4px;width:2.6px;height:2.6px;border-radius:50%;background:var(--blue)}

.card{position:absolute;background:var(--white);box-shadow:0 .5px 2px rgba(0,0,0,.15)}
.card-title{font-size:3.8px;font-weight:700;color:var(--ink);margin-bottom:3px}
</style>
</head>
<body>

<!-- Cover, blue -->
<section class="slide col-l row-1">
  <svg class="abs" style="left:0;top:0" width="329" height="185" viewBox="0 0 329 185">
    <path d="M0 0H329V138C270 150 230 118 160 110C90 102 40 112 0 132Z" fill="#2f7bc4"/>
    <path d="M0 132C40 112 90 102 160 110C230 118 270 150 329 138V142C270 156 230 124 160 116C90 108 40 118 0 136Z" fill="#6d6e71"/>
  </svg>
  <h1 class="cover-title serif">Innovative EPM<br>Solutions for<br>Finance and Beyond</h1>
  <div class="photo" role="img" aria-label="Network globe imagery in deep blue" style="left:197px;top:8px;width:110px;height:144px;background:linear-gradient(160deg,#4b7fb8,#1a2f52 60%,#2a4a7a)"></div>
  <div class="cover-brand">BRANKELL<span class="sub">ADVISORY</span></div>
  <div class="socials"><span></span><span></span><span></span><span></span></div>
</section>

<!-- Cover, light -->
<section class="slide col-r row-1">
  <div class="photo" role="img" aria-label="Soft background of a hand touching a digital network globe" style="left:0;top:0;width:329px;height:185px;background:linear-gradient(120deg,#e6edf3,#d4dde6 55%,#cfd5db)"></div>
  <div class="photo" role="img" aria-label="Network globe imagery in deep blue" style="left:197px;top:38px;width:111px;height:134px;background:linear-gradient(160deg,#4b7fb8,#1a2f52 60%,#2a4a7a)"></div>
  <div class="abs" style="left:13px;top:14px;font-size:7px;font-weight:700;color:var(--blue);letter-spacing:.8px">BRANKELL</div>
  <h1 class="cover-title serif" style="left:13px;top:79px;color:var(--blue-deep)">Innovative EPM<br>Solutions for<br><span style="color:var(--gray)">Finance and Beyond</span></h1>
</section>

<!-- Template header shape reused -->
<!-- Agenda -->
<section class="slide col-l row-2">
  <svg class="header" viewBox="0 0 329 23"><path d="M0 0H260L250 22H0Z" fill="#6d6e71"/><path d="M0 21.5H250L260 0H262L252 23H0Z" fill="#2f7bc4"/></svg>
  <h2 class="header-title serif">Our Agenda</h2>
  <div class="brand-mini"><span class="mark"></span>BRANKELL</div>
  <div class="abs serif" style="left:30px;top:78px;font-size:16px;color:#e8eef6">BRANKELL</div>
  <div class="abs" style="left:164px;top:46px;width:135px">
    <div style="height:29px"><div class="h-item">Content Tite Here</div><p class="p">Lorem ipsum dolor sit amet, consectetur adipiscing elit, do eiusmod tempor incididunt ut labore et dolore magna Ut enim ad minim veniam, quis nostrud</p></div>
    <div style="height:29px"><div class="h-item">Content Tite Here</div><p class="p">Lorem ipsum dolor sit amet, consectetur adipiscing elit, do eiusmod tempor incididunt ut labore et dolore magna Ut enim ad minim veniam, quis nostrud</p></div>
    <div style="height:29px"><div class="h-item">Content Tite Here</div><p class="p">Lorem ipsum dolor sit amet, consectetur adipiscing elit, do eiusmod tempor incididunt ut labore et dolore magna Ut enim ad minim veniam, quis nostrud</p></div>
    <div style="height:29px"><div class="h-item">Content Tite Here</div><p class="p">Lorem ipsum dolor sit amet, consectetur adipiscing elit, do eiusmod tempor incididunt ut labore et dolore magna Ut enim ad minim veniam, quis nostrud</p></div>
  </div>
  <div class="footer-line"></div>
  <div class="footer"><span>© 2021 brankelladvisory | All Rights Reserved</span><span class="page">Page | 02</span></div>
  <div class="base-line"></div>
</section>

<!-- Icon list -->
<section class="slide col-r row-2">
  <svg class="header" viewBox="0 0 329 23"><path d="M0 0H260L250 22H0Z" fill="#6d6e71"/><path d="M0 21.5H250L260 0H262L252 23H0Z" fill="#2f7bc4"/></svg>
  <h2 class="header-title serif" style="left:29px">Add Your Title Here</h2>
  <div class="brand-mini"><span class="mark"></span>BRANKELL</div>
  <div class="icon-dot gray" style="left:28px;top:46px"></div>
  <div class="icon-dot blue" style="left:28px;top:75px"></div>
  <div class="icon-dot gray" style="left:28px;top:104px"></div>
  <div class="icon-dot gray" style="left:28px;top:133px"></div>
  <div class="icon-dot blue" style="left:179px;top:46px"></div>
  <div class="icon-dot gray" style="left:179px;top:75px"></div>
  <div class="icon-dot blue" style="left:179px;top:104px"></div>
  <div class="icon-dot gray" style="left:179px;top:133px"></div>
  <div class="abs" style="left:50px;top:48px;width:105px">
    <div style="height:29px"><div class="h-item">Content Tite Here</div><p class="p">Lorem ipsum dolor sit amet, consectetur adipiscing elit, do eiusmod tempor incididunt ut labore et dolore magna Ut enim</p></div>
    <div style="height:29px"><div class="h-item">Content Tite Here</div><p class="p">Lorem ipsum dolor sit amet, consectetur adipiscing elit, do eiusmod tempor incididunt ut labore et dolore magna Ut enim</p></div>
    <div style="height:29px"><div class="h-item">Content Tite Here</div><p class="p">Lorem ipsum dolor sit amet, consectetur adipiscing elit, do eiusmod tempor incididunt ut labore et dolore magna Ut enim</p></div>
    <div style="height:29px"><div class="h-item">Content Tite Here</div><p class="p">Lorem ipsum dolor sit amet, consectetur adipiscing elit, do eiusmod tempor incididunt ut labore et dolore magna Ut enim</p></div>
  </div>
  <div class="abs" style="left:201px;top:48px;width:105px">
    <div style="height:29px"><div class="h-item">Content Tite Here</div><p class="p">Lorem ipsum dolor sit amet, consectetur adipiscing elit, do eiusmod tempor incididunt ut labore et dolore magna Ut enim</p></div>
    <div style="height:29px"><div class="h-item">Content Tite Here</div><p class="p">Lorem ipsum dolor sit amet, consectetur adipiscing elit, do eiusmod tempor incididunt ut labore et dolore magna Ut enim</p></div>
    <div style="height:29px"><div class="h-item">Content Tite Here</div><p class="p">Lorem ipsum dolor sit amet, consectetur adipiscing elit, do eiusmod tempor incididunt ut labore et dolore magna Ut enim</p></div>
    <div style="height:29px"><div class="h-item">Content Tite Here</div><p class="p">Lorem ipsum dolor sit amet, consectetur adipiscing elit, do eiusmod tempor incididunt ut labore et dolore magna Ut enim</p></div>
  </div>
  <div class="footer-line"></div>
  <div class="footer"><span>© 2021 brankelladvisory | All Rights Reserved</span><span class="page">Page | 03</span></div>
  <div class="base-line"></div>
</section>

<!-- Agenda with photo and bullets -->
<section class="slide col-l row-3">
  <svg class="header" viewBox="0 0 329 23"><path d="M0 0H260L250 22H0Z" fill="#6d6e71"/><path d="M0 21.5H250L260 0H262L252 23H0Z" fill="#2f7bc4"/></svg>
  <h2 class="header-title serif">Our Agenda</h2>
  <div class="brand-mini"><span class="mark"></span>BRANKELL</div>
  <div class="photo" role="img" aria-label="Business meeting in a glass-walled office" style="left:27px;top:37px;width:138px;height:121px;background:linear-gradient(180deg,#b9c2c8,#7e8a92 55%,#4d5a66)"></div>
  <h3 class="abs serif" style="left:186px;top:48px;font-size:8.5px;color:var(--ink)">Add Your Title Here</h3>
  <div class="abs" style="left:186px;top:61px;width:24px;height:1px;background:var(--blue)"></div>
  <ul class="bullets">
    <li>Lorem ipsum dolor sit amet, consectetur adipiscing elit, sed do eiusmod</li>
    <li>tempor incididunt ut labore et dolore magna aliqua.</li>
    <li>Ut enim ad minim veniam, quis nostrud exercitation ullamco</li>
    <li>Laboris nisi ut aliquip ex ea commodo consequat.</li>
    <li>Duis aute irure dolor in reprehenderit in voluptate velit esse</li>
    <li>Cillum dolore eu fugiat nulla pariatur.</li>
    <li>Excepteur sint occaecat cupidatat non proident,</li>
    <li>Sunt in culpa qui officia deserunt mollit anim id est laborum.</li>
    <li>Sed ut perspiciatis unde omnis iste natus error</li>
    <li>Sit voluptatem accusantium doloremque laudantium,</li>
    <li>Totam rem aperiam, eaque ipsa quae ab illo</li>
  </ul>
  <div class="footer-line"></div>
  <div class="footer"><span>© 2021 brankelladvisory | All Rights Reserved</span><span class="page">Page | 04</span></div>
  <div class="base-line"></div>
</section>

<!-- Two columns -->
<section class="slide col-r row-3">
  <svg class="header" viewBox="0 0 329 23"><path d="M0 0H260L250 22H0Z" fill="#6d6e71"/><path d="M0 21.5H250L260 0H262L252 23H0Z" fill="#2f7bc4"/></svg>
  <h2 class="header-title serif">Add Your Title Here</h2>
  <div class="brand-mini"><span class="mark"></span>BRANKELL</div>
  <div class="photo" role="img" aria-label="Three colleagues talking over laptops" style="left:27px;top:39px;width:131px;height:61px;background:linear-gradient(180deg,#c9cdd1,#8c949c)"></div>
  <div class="abs" style="left:27px;top:100px;width:131px;height:60px;background:var(--gray);padding:11px 10px">
    <div class="card-title" style="color:var(--white)">Lorem ipsum dolor sit amet, consectetur</div>
    <p class="p" style="color:#e6e6e6">Sed ut perspiciatis unde omnis iste natus error sit voluptatem accusantium doloremque laudantium, totam rem aperiam, eaque ipsa quae ab illo inventore veritatis et quasi architecto beatae vitae dicta sunt explicabo. Nemo enim ipsam voluptatem quia voluptas sit aspernatur aut odit aut fugit.</p>
  </div>
  <div class="photo" role="img" aria-label="Laptop showing charts on a desk with coffee" style="left:170px;top:39px;width:131px;height:61px;background:linear-gradient(180deg,#e0dcd6,#a8a39c)"></div>
  <div class="abs" style="left:170px;top:100px;width:131px;height:60px;background:var(--blue);padding:11px 10px">
    <div class="card-title" style="color:var(--white)">Lorem ipsum dolor sit amet, consectetur</div>
    <p class="p" style="color:#e6eef8">Sed ut perspiciatis unde omnis iste natus error sit voluptatem accusantium doloremque laudantium, totam rem aperiam, eaque ipsa quae ab illo inventore veritatis et quasi architecto beatae vitae dicta sunt explicabo. Nemo enim ipsam voluptatem quia voluptas sit aspernatur aut odit aut fugit.</p>
  </div>
  <div class="footer-line"></div>
  <div class="footer"><span>© 2021 brankelladvisory | All Rights Reserved</span><span class="page">Page | 05</span></div>
  <div class="base-line"></div>
</section>

<!-- Three columns with photos -->
<section class="slide col-l row-4">
  <svg class="header" viewBox="0 0 329 23"><path d="M0 0H260L250 22H0Z" fill="#6d6e71"/><path d="M0 21.5H250L260 0H262L252 23H0Z" fill="#2f7bc4"/></svg>
  <h2 class="header-title serif">Add Your Title Here</h2>
  <div class="brand-mini"><span class="mark"></span>BRANKELL</div>
  <div class="card" style="left:27px;top:39px;width:87px;height:121px">
    <div class="photo" role="img" aria-label="Laptop with bar charts" style="left:0;top:0;width:87px;height:60px;background:linear-gradient(180deg,#d9dde0,#9da5ab)"></div>
    <div class="abs" style="left:8px;top:72px;width:72px"><div class="card-title">Lorem ipsum dolor sit consectetur</div><p class="p">Sed ut perspiciatis unde omnis iste natus error sit voluptatem accusantium doloremque laudantium, totam rem aperiam, eaque ipsa quae ab illo inventore veritatis et quasi architecto beatae vitae dicta sunt explicabo.</p></div>
  </div>
  <div class="card" style="left:121px;top:39px;width:87px;height:121px">
    <div class="abs" style="left:8px;top:11px;width:72px"><div class="card-title">Lorem ipsum dolor sit consectetur</div><p class="p">Sed ut perspiciatis unde omnis iste natus error sit voluptatem accusantium doloremque laudantium, totam rem aperiam, eaque ipsa quae ab illo inventore veritatis et quasi architecto beatae vitae dicta sunt explicabo.</p></div>
    <div class="photo" role="img" aria-label="Hands writing beside a laptop with charts" style="left:0;top:61px;width:87px;height:60px;background:linear-gradient(180deg,#c7cbcf,#7d858c)"></div>
  </div>
  <div class="card" style="left:215px;top:39px;width:87px;height:121px">
    <div class="photo" role="img" aria-label="Financial reports and calculator on a desk" style="left:0;top:0;width:87px;height:60px;background:linear-gradient(180deg,#4a5866,#a9b8c6)"></div>
    <div class="abs" style="left:8px;top:72px;width:72px"><div class="card-title">Lorem ipsum dolor sit consectetur</div><p class="p">Sed ut perspiciatis unde omnis iste natus error sit voluptatem accusantium doloremque laudantium, totam rem aperiam, eaque ipsa quae ab illo inventore veritatis et quasi architecto beatae vitae dicta sunt explicabo.</p></div>
  </div>
  <div class="footer-line"></div>
  <div class="footer"><span>© 2021 brankelladvisory | All Rights Reserved</span><span class="page">Page | 06</span></div>
  <div class="base-line"></div>
</section>

<!-- Three columns with icons -->
<section class="slide col-r row-4">
  <svg class="header" viewBox="0 0 329 23"><path d="M0 0H260L250 22H0Z" fill="#6d6e71"/><path d="M0 21.5H250L260 0H262L252 23H0Z" fill="#2f7bc4"/></svg>
  <h2 class="header-title serif">Add Your Title Here</h2>
  <div class="brand-mini"><span class="mark"></span>BRANKELL</div>
  <div class="photo" role="img" aria-label="Blue-toned office team backdrop" style="left:0;top:122px;width:329px;height:63px;background:linear-gradient(180deg,#2f7bc4,#2a70b4)"></div>
  <div class="card" style="left:27px;top:54px;width:84px;height:96px;text-align:center;padding:9px 7px 0">
    <svg width="14" height="14" viewBox="0 0 14 14"><circle cx="7" cy="7" r="3" fill="#2f7bc4"/><circle cx="2" cy="2" r="1.6" fill="#6d6e71"/><circle cx="12" cy="2" r="1.6" fill="#6d6e71"/><circle cx="2" cy="12" r="1.6" fill="#6d6e71"/><circle cx="12" cy="12" r="1.6" fill="#6d6e71"/></svg>
    <div class="card-title" style="margin-top:1px">Lorem ipsum dolor</div>
    <p class="p">Sed ut perspiciatis unde omnis iste natus error sit voluptatem accusantium doloremque laudantium, totam rem aperiam, eaque ipsa quae ab illo inventore veritatis et quasi architecto beatae vitae dicta sunt explicabo. Nemo enim ipsam voluptatem quia voluptas sit aspernatur aut odit aut fugit, sed quia consequuntur magni dolores eos qui ratione voluptatem sequi nesciunt.</p>
  </div>
  <div class="card" style="left:122px;top:54px;width:84px;height:96px;text-align:center;padding:9px 7px 0">
    <svg width="14" height="14" viewBox="0 0 14 14"><circle cx="7" cy="8" r="5.5" fill="none" stroke="#6d6e71" stroke-width="1.3"/><circle cx="7" cy="8" r="2.5" fill="#2f7bc4"/><path d="M7 8L2 1" stroke="#2f7bc4" stroke-width="1"/></svg>
    <div class="card-title" style="margin-top:1px">Lorem ipsum dolor</div>
    <p class="p">Sed ut perspiciatis unde omnis iste natus error sit voluptatem accusantium doloremque laudantium, totam rem aperiam, eaque ipsa quae ab illo inventore veritatis et quasi architecto beatae vitae dicta sunt explicabo. Nemo enim ipsam voluptatem quia voluptas sit aspernatur aut odit aut fugit, sed quia consequuntur magni dolores eos qui ratione voluptatem sequi nesciunt.</p>
  </div>
  <div class="card" style="left:217px;top:54px;width:84px;height:96px;text-align:center;padding:9px 7px 0">
    <svg width="14" height="14" viewBox="0 0 14 14"><path d="M2 7L12 2L13 5L3 9Z" fill="#6d6e71"/><path d="M7 7L4 13M7 7L10 13M7 7V13" stroke="#2f7bc4" stroke-width="1"/></svg>
    <div class="card-title" style="margin-top:1px">Lorem ipsum dolor</div>
    <p class="p">Sed ut perspiciatis unde omnis iste natus error sit voluptatem accusantium doloremque laudantium, totam rem aperiam, eaque ipsa quae ab illo inventore veritatis et quasi architecto beatae vitae dicta sunt explicabo. Nemo enim ipsam voluptatem quia voluptas sit aspernatur aut odit aut fugit, sed quia consequuntur magni dolores eos qui ratione voluptatem sequi nesciunt.</p>
  </div>
  <div class="footer on-blue"><span>© 2021 brankelladvisory | All Rights Reserved</span><span class="page">Page | 06</span></div>
</section>

<!-- Four boxes -->
<section class="slide col-l row-5">
  <svg class="header" viewBox="0 0 329 23"><path d="M0 0H260L250 22H0Z" fill="#6d6e71"/><path d="M0 21.5H250L260 0H262L252 23H0Z" fill="#2f7bc4"/></svg>
  <h2 class="header-title serif">Add Your Title Here</h2>
  <div class="brand-mini"><span class="mark"></span>BRANKELL</div>
  <div class="card" style="left:27px;top:41px;width:132px;height:50px">
    <div class="photo" role="img" aria-label="Two colleagues shaking hands" style="left:3px;top:3px;width:48px;height:44px;background:linear-gradient(150deg,#8e8478,#4b4640)"></div>
    <div class="abs" style="left:57px;top:9px;width:70px"><div class="card-title" style="margin-bottom:2px">Lorem ipsum dolor consectetur</div><p class="p">Sed ut perspiciatis unde omnis iste natus error sit voluptatem accusantium doloremque laudantium, totam rem aperiam, eaque ipsa quae ab illo inventore veritatis et quasi architecto beatae vitae</p></div>
  </div>
  <div class="card" style="left:170px;top:41px;width:132px;height:50px">
    <div class="photo" role="img" aria-label="Team handshake at a meeting table" style="left:3px;top:3px;width:48px;height:44px;background:linear-gradient(150deg,#b7bec4,#5c6670)"></div>
    <div class="abs" style="left:57px;top:9px;width:70px"><div class="card-title" style="margin-bottom:2px">Lorem ipsum dolor consectetur</div><p class="p">Sed ut perspiciatis unde omnis iste natus error sit voluptatem accusantium doloremque laudantium, totam rem aperiam, eaque ipsa quae ab illo inventore veritatis et quasi architecto beatae vitae</p></div>
  </div>
  <div class="card" style="left:27px;top:107px;width:132px;height:50px">
    <div class="photo" role="img" aria-label="Colleagues reviewing a tablet together" style="left:3px;top:3px;width:48px;height:44px;background:linear-gradient(150deg,#8a96a4,#2c3a4c)"></div>
    <div class="abs" style="left:57px;top:9px;width:70px"><div class="card-title" style="margin-bottom:2px">Lorem ipsum dolor consectetur</div><p class="p">Sed ut perspiciatis unde omnis iste natus error sit voluptatem accusantium doloremque laudantium, totam rem aperiam, eaque ipsa quae ab illo inventore veritatis et quasi architecto beatae vitae</p></div>
  </div>
  <div class="card" style="left:170px;top:107px;width:132px;height:50px">
    <div class="photo" role="img" aria-label="Two people working at a laptop" style="left:3px;top:3px;width:48px;height:44px;background:linear-gradient(150deg,#a49a90,#4f4a46)"></div>
    <div class="abs" style="left:57px;top:9px;width:70px"><div class="card-title" style="margin-bottom:2px">Lorem ipsum dolor consectetur</div><p class="p">Sed ut perspiciatis unde omnis iste natus error sit voluptatem accusantium doloremque laudantium, totam rem aperiam, eaque ipsa quae ab illo inventore veritatis et quasi architecto beatae vitae</p></div>
  </div>
  <div class="footer-line"></div>
  <div class="footer"><span>© 2021 brankelladvisory | All Rights Reserved</span><span class="page">Page | 07</span></div>
  <div class="base-line"></div>
</section>

<!-- Slide break -->
<section class="slide col-r row-5">
  <div class="photo" role="img" aria-label="Blue-tinted office team backdrop" style="left:0;top:0;width:329px;height:185px;background:radial-gradient(ellipse at 55% 40%,#3a80c2,#2f7bc4 60%,#2a72b8)"></div>
  <h2 class="abs serif" style="left:0;width:329px;top:84px;text-align:center;font-size:16px;color:var(--white);letter-spacing:.8px">Slide Break</h2>
</section>

</body>
</html>
```